Breezeway Climate Business Card Design

Design new, 2 sides, business cards for a residential and light commercial heating, air conditioning contractor.

Target Market(s)

Homeowners, small businesses

Industry/Entity Type

Business

Contact Information for Business Card

Dominic Vasquerelli
Phone - 555-214-6837
Email
Address - PO box 618
Millbrook NJ 07999
Website - www.BreezewayClimateLLC.example

Requirements
Must have
• logo, company colors, standard size with no die cut, so I can use printhaven

```html
<!DOCTYPE html>
<html lang="en">
<head>
<meta charset="utf-8">
<title>Breezeway Climate Business Card</title>
<link href="https://fonts.googleapis.com/css2?family=Lato:wght@400;700&display=swap" rel="stylesheet">
<style>
  :root {
    --crimson: #9c2234;
    --cream: #f7e6b5;
    --orange: #f39a2c;
    --ink: #5c5c5c;
    --paper: #ffffff;
    --backdrop: #ece9e4;
  }
  * { margin: 0; padding: 0; box-sizing: border-box; }
  html, body { width: 1200px; height: 903px; overflow: hidden; }
  body {
    background: var(--backdrop);
    font-family: 'Lato', sans-serif;
    display: flex;
    flex-direction: column;
    align-items: center;
    justify-content: center;
    gap: 36px;
  }
  .card {
    width: 720px;
    height: 411px;
    position: relative;
    box-shadow: 0 6px 18px rgba(0,0,0,0.18);
  }
  .card-front { background: var(--crimson); }
  .card-back { background: var(--paper); }

  .brand-front {
    position: absolute;
    top: 150px; left: 0; right: 0;
    text-align: center;
  }
  .brand-name {
    font-weight: 700;
    font-size: 44px;
    display: inline-flex;
    align-items: center;
    gap: 14px;
  }
  .brand-front .brand-name { color: var(--cream); }
  .brand-dot {
    width: 22px; height: 22px;
    border-radius: 50%;
    background: var(--orange);
    display: inline-block;
  }
  .front-url {
    position: absolute;
    bottom: 44px; left: 0; right: 0;
    text-align: center;
    color: var(--paper);
    font-size: 19px;
    letter-spacing: 0.3px;
  }

  .brand-back {
    position: absolute;
    left: 40px; top: 176px;
  }
  .brand-back .brand-name { color: var(--crimson); font-size: 30px; gap: 10px; }
  .brand-back .brand-dot { width: 16px; height: 16px; }

  .contact {
    position: absolute;
    right: 38px; top: 92px;
    text-align: right;
    color: var(--ink);
  }
  .person-name {
    color: var(--crimson);
    font-weight: 700;
    font-size: 27px;
    margin-bottom: 20px;
    padding-right: 30px;
  }
  .contact-line {
    display: flex;
    justify-content: flex-end;
    align-items: center;
    gap: 10px;
    font-size: 16px;
    line-height: 22px;
  }
  .contact-line svg { width: 14px; height: 14px; flex: none; }
  .address { margin-top: 26px; align-items: flex-start; }
  .address-text { line-height: 22px; }
  .icon-stroke { fill: none; stroke: var(--orange); stroke-width: 1.6; }
  .icon-fill { fill: var(--orange); }
</style>
</head>
<body>
  <section class="card card-front">
    <div class="brand-front">
      <span class="brand-name"><span class="brand-dot"></span>Breezeway Climate</span>
    </div>
    <p class="front-url">www.BreezewayClimateLLC.example</p>
  </section>

  <section class="card card-back">
    <div class="brand-back">
      <span class="brand-name"><span class="brand-dot"></span>Breezeway Climate</span>
    </div>
    <div class="contact">
      <h1 class="person-name">Dominic Vasquerelli</h1>
      <div class="contact-line">
        <span>555-214-6837</span>
        <svg viewBox="0 0 14 14" aria-hidden="true"><path class="icon-fill" d="M3 1l2.2 2.6-1.3 1.6c.8 1.8 2.1 3.1 3.9 3.9l1.6-1.3L12 10l-1.2 2.3C6 12 2 8 1.7 3.2z"/></svg>
      </div>
      <div class="contact-line">
        <span>info@BreezewayClimateLLC.example</span>
        <svg viewBox="0 0 14 14" aria-hidden="true"><rect class="icon-fill" x="1" y="3" width="12" height="8" rx="1"/><path d="M1.5 3.5L7 8l5.5-4.5" fill="none" stroke="#fff" stroke-width="1.2"/></svg>
      </div>
      <div class="contact-line">
        <span>www.BreezewayClimateLLC.example</span>
        <svg viewBox="0 0 14 14" aria-hidden="true"><circle class="icon-stroke" cx="7" cy="7" r="5.6"/><ellipse class="icon-stroke" cx="7" cy="7" rx="2.4" ry="5.6"/><path class="icon-stroke" d="M1.4 7h11.2"/></svg>
      </div>
      <div class="contact-line address">
        <span class="address-text">PO box 618<br>Millbrook NJ 07999</span>
        <svg viewBox="0 0 14 14" aria-hidden="true"><path class="icon-fill" d="M7 .8a4.6 4.6 0 0 0-4.6 4.6C2.4 9 7 13.4 7 13.4s4.6-4.4 4.6-8A4.6 4.6 0 0 0 7 .8zm0 6.4a1.8 1.8 0 1 1 0-3.6 1.8 1.8 0 0 1 0 3.6z"/></svg>
      </div>
    </div>
  </section>
</body>
</html>
```